Special release wine label

Marrow Creek Vineyards is a small premium wine producer in the Barossa - South Australia. We are a five star rated winery, producing exceptional wines true to variety, region and house style. We have a very special parcel of wine that we wish to release as an exclusive wine. Visit www.marrowcreekvineyards.com.au for further feel.

The wine will be called Marrow Creek Vineyards, 2012, The Quiet Harvest Shiraz - Cabernet.

The wine can be bottled in either a burgundy or Bordeaux shaped bottle

Industry/Entity Type

House

```html
<!DOCTYPE html>
<html lang="en">
<head>
<meta charset="utf-8">
<title>Marrow Creek Vineyards – Special Release Label Proposal</title>
<link href="https://fonts.googleapis.com/css2?family=Montserrat:wght@700&family=Questrial&family=Cinzel:wght@700&family=Tinos:wght@400;700&family=Nothing+You+Could+Do&display=swap" rel="stylesheet">
<style>
  :root {
    --paper: #ffffff;
    --ink: #111111;
    --night: #000000;
    --gold: #d4b21c;
    --gold-soft: #e6cd5a;
    --red: #e5262b;
    --frame: #3a3a3a;
    --caption-light: #ffffff;
  }
  html, body { margin: 0; padding: 0; overflow: hidden; background: var(--paper); }
  .board {
    position: relative; width: 1200px; height: 1000px; overflow: hidden;
    background: linear-gradient(to bottom, var(--paper) 0 648px, var(--night) 648px 100%);
    font-family: "Questrial", "Century Gothic", sans-serif; color: var(--ink);
  }
  .board-title {
    position: absolute; left: 34px; top: 16px; margin: 0;
    font-family: "Montserrat", Arial, sans-serif; font-weight: 700; font-size: 40px; letter-spacing: -0.5px;
  }
  .brief-notes { position: absolute; left: 34px; top: 102px; width: 435px; }
  .brief-notes p { margin: 0 0 22px; font-size: 17px; line-height: 21px; text-align: justify; }
  .brief-notes p:nth-child(2) { margin-bottom: 30px; }

  .bottle-render {
    position: absolute; left: 75px; top: 462px; width: 353px; height: 353px;
    background: radial-gradient(ellipse at 50% 55%, #5a5a5a 0%, #2a2a2a 38%, #e9e9e9 70%, #f6f6f6 100%);
  }
  .caption { position: absolute; margin: 0; font-size: 17px; line-height: 21px; text-align: center; }
  .caption--light { color: var(--caption-light); }
  .caption--bottles { left: 75px; top: 822px; width: 353px; }
  .caption--bordeaux { left: 540px; top: 404px; width: 240px; }
  .caption--burgundy { left: 528px; top: 806px; width: 280px; }
  .caption--back { left: 830px; top: 728px; width: 335px; }
  .caption--barcode { left: 826px; top: 24px; width: 342px; }

  /* Front labels */
  .front-label {
    position: absolute; background: var(--paper); border: 1px solid var(--frame);
    text-align: center; box-sizing: border-box;
  }
  .front-label > * { position: absolute; left: 0; right: 0; margin: 0; }
  .front-label--bordeaux { left: 554px; top: 22px; width: 213px; height: 369px; }
  .front-label--burgundy { left: 527px; top: 487px; width: 283px; height: 299px; }
  .wordmark { font-family: "Cinzel", serif; font-weight: 700; color: var(--gold); letter-spacing: 1.5px; }
  .homestead-art {
    left: auto; right: auto; margin: 0 auto;
    background: radial-gradient(ellipse at 50% 55%, var(--gold) 0%, var(--gold-soft) 55%, rgba(230,205,90,0.25) 100%);
  }
  .region { font-family: "Tinos", serif; letter-spacing: 3px; }
  .release { font-family: "Tinos", serif; letter-spacing: 2.5px; }
  .wine-line { font-family: "Tinos", serif; color: var(--red); letter-spacing: 1.5px; }
  .vintage { font-family: "Tinos", serif; letter-spacing: 2.5px; }

  .front-label--bordeaux .wordmark--top { top: 16px; font-size: 16px; }
  .front-label--bordeaux .homestead-art { top: 72px; left: 46px; width: 120px; height: 100px; }
  .front-label--bordeaux .wordmark--bottom { top: 192px; font-size: 17px; }
  .front-label--bordeaux .region { top: 226px; font-size: 15px; }
  .front-label--bordeaux .release { top: 244px; font-size: 10.5px; }
  .front-label--bordeaux .wine-line--sub { top: 276px; font-size: 10px; }
  .front-label--bordeaux .wine-line--main { top: 288px; font-size: 14px; }
  .front-label--bordeaux .vintage { top: 319px; font-size: 16px; }

  .front-label--burgundy .wordmark--top { top: 14px; font-size: 14px; }
  .front-label--burgundy .homestead-art { top: 56px; left: 63px; width: 125px; height: 85px; }
  .front-label--burgundy .wordmark--bottom { top: 152px; font-size: 15px; }
  .front-label--burgundy .region { top: 184px; font-size: 15px; }
  .front-label--burgundy .release { top: 200px; font-size: 10.5px; }
  .front-label--burgundy .wine-line--sub { top: 223px; font-size: 10px; }
  .front-label--burgundy .wine-line--main { top: 235px; font-size: 14px; }
  .front-label--burgundy .vintage { top: 258px; font-size: 16px; }

  /* Back labels */
  .back-label {
    position: absolute; left: 890px; width: 215px; height: 297px; box-sizing: border-box;
    background: var(--paper); border: 1px solid var(--frame);
  }
  .back-label--with-barcode { top: 97px; }
  .back-label--plain { top: 411px; }
  .back-label > * { position: absolute; margin: 0; }
  .back-label .wine-line--sub { left: 0; right: 0; top: 9px; text-align: center; font-size: 9.5px; }
  .back-label .wine-line--main { left: 0; right: 0; top: 20px; text-align: center; font-size: 13.5px; }
  .tasting-note { left: 10px; right: 10px; font-size: 6.4px; line-height: 9.3px; text-align: center; }
  .tasting-note--soil { top: 38px; }
  .tasting-note--vintage { top: 86px; }
  .tagline { left: 8px; right: 6px; top: 129px; font-family: "Tinos", serif; font-weight: 700; font-size: 6.6px; letter-spacing: 0.2px; }
  .producer { left: 12px; top: 141px; font-size: 5.6px; line-height: 8.3px; text-transform: uppercase; }
  .producer .web { text-transform: none; }
  .sulphites { left: 12px; top: 219px; font-size: 5.6px; }
  .volume { left: 12px; top: 252px; font-size: 9.5px; }
  .origin { left: 12px; top: 264px; font-family: "Tinos", serif; font-weight: 700; font-size: 9.5px; color: var(--red); }
  .country { left: 12px; top: 276px; font-size: 7px; }
  .back-label .wordmark { font-size: 8px; letter-spacing: 0.8px; left: 118px; width: 90px; text-align: center; }
  .back-label .homestead-art { left: 137px; width: 52px; }
  .back-label--with-barcode .wordmark--top { top: 145px; }
  .back-label--with-barcode .homestead-art { top: 169px; height: 42px; }
  .back-label--with-barcode .wordmark--bottom { top: 230px; }
  .barcode-area { left: 130px; top: 244px; width: 68px; height: 41px; background: var(--gold); }
  .back-label--plain .wordmark--top { top: 164px; }
  .back-label--plain .homestead-art { top: 190px; height: 46px; }
  .back-label--plain .wordmark--bottom { top: 251px; }

  .disclaimer {
    position: absolute; left: 12px; margin: 0; color: var(--caption-light);
    font-family: "Nothing You Could Do", cursive; font-size: 27px; letter-spacing: 1.5px;
  }
  .disclaimer--change { top: 912px; }
  .disclaimer--illustration { top: 951px; }
</style>
</head>
<body>
<main class="board">
  <h1 class="board-title">Marrow Creek Vineyards</h1>

  <section class="brief-notes">
    <p>Proposed print of the label will be definately a gold foil printing on the golden yellow area such as the logo of Marrow Creek Vineyards and also a red foil (if available) for the name of the wine which is The Quiet Harvest Shiraz Cabernet</p>
    <p>Detail of the wine which located at the back label maybe changed and altered and other details which are lacking or wrong can be else corrected by me or by you.</p>
    <p>Wordings of all text which are in the proposed design is either or bigger than 2mm which is the standard requirement that is needed by the US guideline for labelling on alchohol products.</p>
  </section>

  <div class="bottle-render" role="img" aria-label="Render of three dark wine bottles wearing the proposed front and back labels"></div>
  <p class="caption caption--light caption--bottles">Top : Artist impression of &nbsp;propsed design for the bottles</p>

  <article class="front-label front-label--bordeaux">
    <p class="wordmark wordmark--top">MARROW CREEK</p>
    <div class="homestead-art" role="img" aria-label="Gold foil line drawing of the vineyard homestead"></div>
    <p class="wordmark wordmark--bottom">VINEYARDS</p>
    <p class="region">BAROSSA VALLEY</p>
    <p class="release">SPECIAL RELEASE</p>
    <p class="wine-line wine-line--sub">THE QUIET HARVEST</p>
    <p class="wine-line wine-line--main">SHIRAZ CABERNET</p>
    <p class="vintage">2012</p>
  </article>
  <p class="caption caption--bordeaux">Top : &nbsp;Propsed design for the Bordeaux bottle<br>75mm (W) x 130mm (H)</p>

  <article class="front-label front-label--burgundy">
    <p class="wordmark wordmark--top">MARROW CREEK</p>
    <div class="homestead-art" role="img" aria-label="Gold foil line drawing of the vineyard homestead"></div>
    <p class="wordmark wordmark--bottom">VINEYARDS</p>
    <p class="region">BAROSSA VALLEY</p>
    <p class="release">SPECIAL RELEASE</p>
    <p class="wine-line wine-line--sub">THE QUIET HARVEST</p>
    <p class="wine-line wine-line--main">SHIRAZ CABERNET</p>
    <p class="vintage">2012</p>
  </article>
  <p class="caption caption--light caption--burgundy">Top : &nbsp;Propsed design for the Burgundy bottle<br>100mm (W) x 105mm (H)</p>

  <p class="caption caption--barcode">Bottom : Golden-yellow coloured box highlighted will be the propsed are for barcode if available</p>

  <article class="back-label back-label--with-barcode">
    <p class="wine-line wine-line--sub">THE QUIET HARVEST</p>
    <p class="wine-line wine-line--main">SHIRAZ CABERNET</p>
    <p class="tasting-note tasting-note--soil">Rich, fertile, sandy loam and dark biscay soils provide ideal growing opportunities for vines. The Barossa has a Mediterranean-like climate, warm summers and cold winters further in enhance the viticultural conditions.</p>
    <p class="tasting-note tasting-note--vintage">The 2012 vintage produced beautiful ripe fruit, with exceptional depth of colour, flavour and natural tannins. Baume reached 14 degrees before the fruit was picked and delivered to the winery ready for crushing and fermenting.</p>
    <p class="tagline">TASTE THE DEPTH AND DIVERSITY OF THE &nbsp;BAROSSA</p>
    <p class="producer">Produced and bottled by<br>Marrow Creek Vineyards<br>C/o Halden Post Office<br>Halden,<br>South Australia, 5299<br><span class="web">http://www.marrowcreekvineyards.com.au</span></p>
    <p class="wordmark wordmark--top">MARROW CREEK</p>
    <div class="homestead-art" role="img" aria-label="Gold foil line drawing of the vineyard homestead"></div>
    <p class="sulphites">Contains Sulphites</p>
    <p class="wordmark wordmark--bottom">VINEYARDS</p>
    <p class="volume">14.0% VOL &nbsp;&nbsp;75 cl</p>
    <p class="origin">SOUTH AUSTRALIA</p>
    <p class="country">WINE OF AUSTRALIA</p>
    <div class="barcode-area"></div>
  </article>

  <article class="back-label back-label--plain">
    <p class="wine-line wine-line--sub">THE QUIET HARVEST</p>
    <p class="wine-line wine-line--main">SHIRAZ CABERNET</p>
    <p class="tasting-note tasting-note--soil">Rich, fertile, sandy loam and dark biscay soils provide ideal growing opportunities for vines. The Barossa has a Mediterranean-like climate, warm summers and cold winters further in enhance the viticultural conditions.</p>
    <p class="tasting-note tasting-note--vintage">The 2012 vintage produced beautiful ripe fruit, with exceptional depth of colour, flavour and natural tannins. Baume reached 14 degrees before the fruit was picked and delivered to the winery ready for crushing and fermenting.</p>
    <p class="tagline">TASTE THE DEPTH AND DIVERSITY OF THE &nbsp;BAROSSA</p>
    <p class="producer">Produced and bottled by<br>Marrow Creek Vineyards<br>C/o Halden Post Office<br>Halden,<br>South Australia, 5299<br><span class="web">http://www.marrowcreekvineyards.com.au</span></p>
    <p class="wordmark wordmark--top">MARROW CREEK</p>
    <div class="homestead-art" role="img" aria-label="Gold foil line drawing of the vineyard homestead"></div>
    <p class="sulphites">Contains Sulphites</p>
    <p class="wordmark wordmark--bottom">VINEYARDS</p>
    <p class="volume">14.0% VOL &nbsp;&nbsp;75 cl</p>
    <p class="origin">SOUTH AUSTRALIA</p>
    <p class="country">WINE OF AUSTRALIA</p>
  </article>
  <p class="caption caption--light caption--back">Top : &nbsp;Propsed design Back Labelling<br>75mm (W) x 105mm (H)</p>

  <p class="disclaimer disclaimer--change">* &nbsp;Details in artwork or design are subjected to change</p>
  <p class="disclaimer disclaimer--illustration">* &nbsp;Artwork is for illustration purposes only</p>
</main>
</body>
</html>
```